Price list for young Relaxon clinic

I require a price list/Treatment menu for clinic

To include:
Logo
Address
Phone number
Website

List of services and Prices
Relaxon 1 area £100
Relaxon 2 areas £150
Relaxon 3 areas £200
Lip Enhancement 0.5ml £100
Lip Enhancement 1ml £200
Facial Fillers £200 per 1ml
Volumiq £450 per session (2 vials - must be bought as a course)
Non Surgical Face Lift (Thread Lift) £600 per area
Skin Press Full Face £250
Skin Press Small Per Small Area £100
Cryo Therapy £60
Chemical Peel Light Peel and Microdermabrasion £85
Chemical Peel Deep Peel £150
Consultation £30 redeemable against service
Relaxon Top Up Relaxon £50 (must be within 2 weeks of 1st treatment)
Filler Top Up £100 (must be within 2 weeks of 1st appointment)

Open Hours
Updates

Company Name: HVM Address: 482 Pellbrook Road, 6 Warnford High Street, KT4 3JQ Phone: 0208 947 2186 Website: www.hollyvanmereaesthetics.co.uk

Please add more colour

Needs to be much cleaner and simpler Front page to include logo and price list Back page to inculde open hours and contact information including google map. Please no images with needles. Images of lips and faces are good, but try not to crowd copy on the pagei. No copy on top of images. White, grey, black and reds are good on colouring.

Target Market(s)

young market ages 22-45 years old mainly female
modern

Industry/Entity Type

Clinic

Number of Pages Required

4 page

Requirements
Must have
• Logo - logo must be in colour grey/silver
• Address (small map?)
• Phone number
• Web address
• Services
• Open hours
• Prices
• Images

```html
<!DOCTYPE html>
<html lang="en">
<head>
<meta charset="utf-8">
<title>Holly Vanmere Aesthetics – Services and Prices</title>
<link rel="stylesheet" href="https://fonts.googleapis.com/css2?family=Crimson+Text:wght@400;600;700&display=swap">
<style>
  :root{
    --paper-top:#ffffff;
    --paper-bottom:#dcdcdc;
    --ornament:#c9c9c9;
    --ornament-soft:#d6d6d6;
    --ink:#6f6f6f;
    --ink-dark:#5f5f5f;
    --badge:#696969;
    --badge-text:#ffffff;
  }
  *{margin:0;padding:0;box-sizing:border-box}
  html,body{width:927px;height:1200px;overflow:hidden}
  body{font-family:"Crimson Text",Georgia,serif;color:var(--ink)}
  .sheet{
    position:relative;width:927px;height:1200px;overflow:hidden;
    background:linear-gradient(180deg,var(--paper-top) 0%,var(--paper-top) 26%,var(--paper-bottom) 100%);
  }
  .ornament-band{
    position:absolute;left:0;top:0;width:927px;height:200px;
    background:linear-gradient(180deg,var(--ornament-soft) 0%,rgba(214,214,214,0.35) 75%,rgba(255,255,255,0) 100%);
  }
  .ornament-circle{
    position:absolute;border-radius:50%;
    background:radial-gradient(circle,var(--ornament-soft) 0%,var(--ornament) 100%);
  }
  .ornament-circle.left{left:-296px;top:334px;width:490px;height:480px}
  .ornament-circle.right{left:736px;top:334px;width:480px;height:480px}
  .brand{position:absolute;left:0;top:156px;width:927px;text-align:center}
  .brand-mark{
    width:78px;height:78px;margin:0 auto;border-radius:50%;
    background:var(--badge);color:var(--badge-text);
    font-size:27px;line-height:78px;letter-spacing:2px;font-weight:400;
  }
  .brand-name-top{margin-top:22px;font-size:17px;letter-spacing:3px;line-height:18px;color:var(--ink)}
  .brand-name-main{font-size:28px;letter-spacing:3.5px;line-height:30px;color:var(--ink-dark)}
  .contact{position:absolute;left:0;top:313px;width:927px;text-align:center;font-size:14.5px;line-height:22px;color:var(--ink)}
  .section-title{
    position:absolute;left:0;top:368px;width:927px;
    display:flex;justify-content:center;align-items:center;gap:10px;
    font-size:23px;color:var(--ink-dark);letter-spacing:0.3px;
  }
  .title-rule{display:block}
  .price-list{position:absolute;left:204px;top:412px;width:560px;list-style:none}
  .price-list li{position:relative;height:34.4px;line-height:34.4px;font-size:14.5px;font-weight:700;color:var(--ink)}
  .price-list li.item::before{
    content:"";position:absolute;left:-5px;top:14px;width:8px;height:6px;border-radius:50%;background:var(--ink-dark);
  }
  .price-list .service{position:absolute;left:16px}
  .price-list .price{position:absolute;left:422px;white-space:nowrap}
  .open-hours{position:absolute;left:387px;top:1124px;font-size:25px;color:var(--ink)}
</style>
</head>
<body>
<main class="sheet">
  <div class="ornament-band" role="img" aria-label="Grey scrolling flourish ornament across the top"></div>
  <div class="ornament-circle left" role="img" aria-label="Circular grey swirl ornament"></div>
  <div class="ornament-circle right" role="img" aria-label="Circular grey swirl ornament"></div>

  <header class="brand">
    <div class="brand-mark">HVM</div>
    <div class="brand-name-top">HOLLY VANMERE</div>
    <div class="brand-name-main">AESTHETICS</div>
  </header>

  <p class="contact">
    Address line 1, Address line 2 , phone : 0208 947 2186, Fax : 0208 947 2187<br>
    E-mail : info@hollyvanmereaesthetics.co.uk, website : www.hollyvanmereaesthetics.co.uk
  </p>

  <h1 class="section-title">
    <svg class="title-rule" width="58" height="10" viewBox="0 0 58 10"><line x1="0" y1="5" x2="44" y2="5" stroke="#6f6f6f" stroke-width="1"/><path d="M44 5 L51 1.5 L58 5 L51 8.5 Z" fill="#6f6f6f"/></svg>
    <span>LIST OF SERVICES AND PRICES</span>
    <svg class="title-rule" width="58" height="10" viewBox="0 0 58 10"><path d="M0 5 L7 1.5 L14 5 L7 8.5 Z" fill="#6f6f6f"/><line x1="14" y1="5" x2="58" y2="5" stroke="#6f6f6f" stroke-width="1"/></svg>
  </h1>

  <ul class="price-list">
    <li class="item"><span class="service">Relaxon 1 area</span><span class="price">£100</span></li>
    <li class="item"><span class="service">Relaxon 2 areas</span><span class="price">£150</span></li>
    <li class="item"><span class="service">Relaxon 3 areas</span><span class="price">£200</span></li>
    <li class="item"><span class="service">Lip Enhancement 0.5ml</span><span class="price">£100</span></li>
    <li class="item"><span class="service">Lip Enhancement 1ml</span><span class="price">£200</span></li>
    <li class="item"><span class="service">Facial Fillers</span><span class="price">£200 per 1ml</span></li>
    <li class="item"><span class="service">Volumiq</span><span class="price">£450 per session</span></li>
    <li class="note"><span class="service">(2 vials - must be bought as a course)</span></li>
    <li class="item"><span class="service">Non Surgical Face Lift (Thread Lift)</span><span class="price">£600 per area</span></li>
    <li class="item"><span class="service">Skin Press Full Face</span><span class="price">£250</span></li>
    <li class="item"><span class="service">Skin Press Small Per Small Area</span><span class="price">£100</span></li>
    <li class="item"><span class="service">Cryo Therapy</span><span class="price">£60</span></li>
    <li class="item"><span class="service">Chemical Peel Light Peel and Microdermabrasion</span><span class="price">£85</span></li>
    <li class="item"><span class="service">Chemical Peel Deep Peel</span><span class="price">£150</span></li>
    <li class="item"><span class="service">Consultation</span><span class="price">£30</span></li>
    <li class="note"><span class="service">redeemable against service</span></li>
    <li class="item"><span class="service">Relaxon Top Up Relaxon</span><span class="price">£50</span></li>
    <li class="note"><span class="service">(must be within 2 weeks of 1st treatment)</span></li>
    <li class="item"><span class="service">Filler Top Up</span><span class="price">£100</span></li>
    <li class="note"><span class="service">(must be within 2 weeks of 1st appointment)</span></li>
  </ul>

  <p class="open-hours">Open Hours&nbsp; :</p>
</main>
</body>
</html>
```